Lucky Lark Roasters

We need a website to sell coffee with a horse theme. We already have a logo and have designed 4 different coffee bags/flavors so far, each of which will be available in ground or whole bean. The brand is intended to be light hearted/whimsical.

Coding

Coded - Design and coding required

Number of Pages Required

4 page

Requirements
Must have
• incorporation of attached photos
Nice to have
• underlying background theme with sky/grass

```html
<!DOCTYPE html>
<html lang="en">
<head>
<meta charset="UTF-8">
<title>Lucky Lark Roasters</title>
<link href="https://fonts.googleapis.com/css2?family=Lexend:wght@400;500;600;700&family=Inter:wght@400;500;600&display=swap" rel="stylesheet">
<style>
:root{
  --cream:#faeedd;
  --cream-2:#f1e6d3;
  --band:#ede6d6;
  --brown:#3b2719;
  --brown-deep:#2c1b10;
  --ink:#24160d;
  --muted:#6e5b4c;
  --accent:#e58b55;
  --light-text:#f6e9d6;
}
*{margin:0;padding:0;box-sizing:border-box}
html,body{width:1200px;height:3592px;overflow:hidden}
body{background:var(--cream);font-family:"Inter",sans-serif;color:var(--ink);position:relative}
section,header,footer{position:relative;width:1200px;overflow:hidden}
h1,h2,h3{font-family:"Lexend",sans-serif;font-weight:600;letter-spacing:-.5px}
.eyebrow{font-family:"Lexend",sans-serif;font-size:12px;font-weight:600;letter-spacing:1px;text-transform:uppercase}
.btn{display:inline-block;background:var(--accent);color:#fff;font-size:13px;font-weight:500;padding:11px 22px;border-radius:3px}
.ph{position:absolute}
p{font-size:13px;line-height:1.6;color:var(--muted)}

/* hero */
.hero{height:560px;background:linear-gradient(180deg,#4a3a26 0%,#6a4a2d 45%,#8a5a35 70%,#3a2214 100%)}
.hero .ph{inset:0;background:radial-gradient(ellipse at 55% 55%,#c9bfae 0%,#8a6846 30%,rgba(60,36,20,.2) 70%),linear-gradient(180deg,#38402a 0%,#5b4128 50%,#3a2214 100%)}
.hero::after{content:"";position:absolute;inset:0;background:rgba(25,14,8,.35)}
.nav{position:absolute;top:0;left:0;right:0;height:58px;display:flex;align-items:center;padding:0 80px;z-index:2}
.brand{font-family:"Lexend",sans-serif;font-weight:700;font-size:19px;color:var(--ink);display:flex;align-items:center;gap:10px;background:var(--cream);padding:8px 14px;border-radius:4px}
.brand i{width:14px;height:14px;border-radius:50%;background:var(--accent);display:block}
.nav ul{list-style:none;display:flex;gap:42px;margin-left:auto;margin-right:40px}
.nav li{color:#fff;font-size:13px}
.hero-copy{position:absolute;top:215px;left:0;right:0;text-align:center;color:#fff;z-index:2}
.hero-copy .eyebrow{color:#fff;margin-bottom:14px}
.hero-copy h1{font-size:44px;line-height:1.2;margin-bottom:22px}

/* features */
.features{height:200px;background:var(--band);display:flex;gap:30px;padding:60px 190px 0}
.feature{width:185px}
.feature svg{width:26px;height:26px;stroke:var(--ink);fill:none;stroke-width:1.6;margin-bottom:8px}
.feature h3{font-size:15px;font-weight:500;margin-bottom:4px}
.feature p{font-size:11px;line-height:1.45}

/* about */
.about{height:560px;background:var(--cream)}
.about-copy{position:absolute;left:190px;top:70px;width:270px}
.about-copy .eyebrow{margin-bottom:10px}
.about-copy h2{font-size:44px;line-height:1.12;margin-bottom:20px}
.about-copy p{margin-bottom:12px;font-size:11px}
.about-copy .btn{margin-top:14px}

/* products */
.products{height:700px;background:var(--brown);text-align:center;color:var(--light-text)}
.products .eyebrow{padding-top:80px;color:var(--light-text)}
.products h2{font-size:40px;margin-top:6px}
.cards{position:absolute;top:200px;left:120px;display:flex;gap:40px}
.card{width:210px;height:430px;background:var(--cream-2);border-radius:3px;position:relative}
.card .ph{left:14px;right:14px;top:14px;height:340px;background:linear-gradient(180deg,#f6ead6 0%,#f6ead6 42%,#dba06a 42%,#c9884f 100%)}
.card .shop{position:absolute;bottom:22px;left:50%;transform:translateX(-50%);font-size:11px;color:var(--ink);border:1px solid var(--ink);padding:7px 18px;border-radius:2px}
.card.active .shop{background:var(--accent);color:#fff;border-color:var(--accent)}

/* testimonials */
.testimonials{height:380px;background:var(--cream)}
.t-head{position:absolute;left:190px;top:60px}
.t-head h2{font-size:44px;line-height:1.12;margin-top:8px}
.avatars{position:absolute;left:200px;top:218px;display:flex;gap:12px}
.avatars span{width:66px;height:66px;border-radius:50%;background:linear-gradient(135deg,#e6c7a6,#b98c66);display:block}
.who{position:absolute;left:268px;top:300px;text-align:center}
.who b{display:block;font-size:13px;font-weight:600}
.who small{font-size:11px;color:var(--muted)}
.quote{position:absolute;left:500px;top:225px;width:520px}
.quote p{font-size:12px;margin-bottom:10px}
.arrows{position:absolute;left:506px;top:335px;display:flex;gap:10px}
.arrows span{width:30px;height:30px;border-radius:50%;border:1px solid var(--ink);display:flex;align-items:center;justify-content:center}
.arrows svg{width:12px;height:12px;stroke:var(--ink);fill:none;stroke-width:2}

/* newsletter */
.newsletter{height:500px;text-align:center;color:#fff}
.newsletter .ph{inset:0;background:radial-gradient(ellipse at 80% 40%,#6a3f22 0%,transparent 45%),radial-gradient(ellipse at 15% 70%,#5a3820 0%,transparent 45%),linear-gradient(180deg,#3e281a,#2a190f)}
.newsletter::after{content:"";position:absolute;inset:0;background:rgba(20,12,6,.35)}
.nl-copy{position:absolute;top:175px;left:0;right:0;z-index:2}
.nl-copy h2{font-size:40px;margin:8px 0 26px;line-height:1.2}
.nl-form{width:400px;height:40px;margin:0 auto;background:#fff;border-radius:3px;display:flex;align-items:center;padding:0 6px 0 16px}
.nl-form span{font-size:12px;color:#9a8a7c;flex:1;text-align:left}
.nl-form b{font-size:12px;font-weight:600;color:var(--ink)}

/* instagram */
.insta{height:340px;background:var(--cream)}
.insta-band{position:absolute;left:200px;top:40px;width:800px;height:72px;background:var(--band);display:flex;align-items:center;justify-content:center;gap:12px;font-family:"Lexend",sans-serif;font-size:26px;font-weight:500}
.insta-band i{width:22px;height:22px;border-radius:4px;background:var(--ink);display:block}
.gallery{position:absolute;left:0;right:0;top:140px;height:170px;display:flex;gap:6px}
.gallery div{flex:1;height:100%}

/* footer */
.footer{height:352px;background:var(--brown-deep);color:var(--light-text)}
.f-intro{position:absolute;left:80px;top:40px;width:300px}
.f-intro h2{font-size:40px;margin:8px 0 16px}
.f-intro p{color:#bba995;font-size:11px}
.f-col{position:absolute;top:60px;display:flex;gap:12px}
.f-col .ic{width:36px;height:36px;border-radius:50%;border:1px solid #7a6552;display:flex;align-items:center;justify-content:center;flex-shrink:0}
.f-col svg{width:15px;height:15px;stroke:var(--light-text);fill:none;stroke-width:1.6}
.f-col h3{font-size:15px;font-weight:500;margin:8px 0 8px}
.f-col p{color:#bba995;font-size:11px;line-height:1.6}
.socials{position:absolute;right:80px;top:60px;display:flex;flex-direction:column;gap:10px}
.socials span{width:26px;height:26px;border-radius:50%;border:1px solid #7a6552;display:block}
.f-bottom{position:absolute;left:80px;right:80px;top:300px;border-top:1px solid #4e3a2b;padding-top:14px;display:flex;font-size:11px;color:#bba995}
.f-bottom ul{list-style:none;display:flex;gap:28px;margin-left:auto}
.to-top{position:absolute;right:80px;top:280px;width:26px;height:26px;background:var(--accent);border-radius:3px;display:flex;align-items:center;justify-content:center}
.to-top svg{width:12px;height:12px;stroke:#fff;fill:none;stroke-width:2}
</style>
</head>
<body>

<header class="hero">
  <div class="ph" role="img" aria-label="White coffee mug on a pile of roasted coffee beans with a burlap sack and leaves"></div>
  <nav class="nav">
    <div class="brand"><i></i>Lucky Lark Roasters</div>
    <ul><li>Home</li><li>Products</li><li>About Us</li><li>Reviews</li></ul>
    <span class="btn">Contact us</span>
  </nav>
  <div class="hero-copy">
    <div class="eyebrow">Lucky Lark Roasters</div>
    <h1>Premium quality service<br>and products</h1>
    <span class="btn">Our products</span>
  </div>
</header>

<section class="features">
  <div class="feature">
    <svg viewBox="0 0 24 24"><rect x="3" y="7" width="18" height="13" rx="2"/><path d="M8 7V5h8v2"/></svg>
    <h3>Fresh products</h3><p>Small batches roasted each week and sent out fresh.</p>
  </div>
  <div class="feature">
    <svg viewBox="0 0 24 24"><circle cx="12" cy="12" r="9"/><path d="M12 7v10M9 10h5a2 2 0 010 4h-5"/></svg>
    <h3>Best price</h3><p>Fair prices on every bag, ground or whole bean.</p>
  </div>
  <div class="feature">
    <svg viewBox="0 0 24 24"><path d="M3 12l9-9h9v9l-9 9z"/><circle cx="16" cy="8" r="1.5"/></svg>
    <h3>Special discounts</h3><p>Regular offers for members and loyal customers.</p>
  </div>
  <div class="feature">
    <svg viewBox="0 0 24 24"><path d="M4 14v-2a8 8 0 0116 0v2"/><rect x="3" y="14" width="4" height="6" rx="1"/><rect x="17" y="14" width="4" height="6" rx="1"/></svg>
    <h3>Live support</h3><p>Friendly help whenever you have a question.</p>
  </div>
</section>

<section class="about">
  <div class="ph" role="img" aria-label="Cartoon rider on a horse" style="left:70px;top:70px;width:100px;height:110px;background:#e6d2b6;border-radius:6px"></div>
  <div class="about-copy">
    <div class="eyebrow">Welcome to Lucky Lark</div>
    <h2>Enjoy the best high quality coffee</h2>
    <p>Our beans are sourced from small farms and roasted with care, so every cup tastes bright, smooth and full of life from the very first sip.</p>
    <p>Pick your favourite blend in ground or whole bean.</p>
    <span class="btn">Discover more</span>
  </div>
  <div class="ph" role="img" aria-label="Coffee beans and brewing tools on a dark table" style="left:672px;top:64px;width:330px;height:216px;background:linear-gradient(135deg,#5a4232,#2f2118)"></div>
  <div class="ph" role="img" aria-label="Smiling woman holding a cup of coffee" style="left:532px;top:248px;width:270px;height:232px;background:linear-gradient(135deg,#d6a778,#8a5a38)"></div>
  <div class="ph" role="img" aria-label="Cup of black coffee on a saucer" style="left:802px;top:280px;width:120px;height:130px;background:linear-gradient(180deg,#eae2d6,#bfb3a3)"></div>
  <div class="ph" role="img" aria-label="Cartoon cowboy riding a rearing horse" style="left:1020px;top:400px;width:130px;height:160px;background:#e6d2b6;border-radius:6px"></div>
</section>

<section class="products">
  <div class="eyebrow">Our products</div>
  <h2>Discover your perfect brews</h2>
  <div class="cards">
    <div class="card"><div class="ph" role="img" aria-label="Coffee bag with horse illustration, first blend"></div><span class="shop">Shop now</span></div>
    <div class="card active"><div class="ph" role="img" aria-label="Coffee bag with horse illustration, second blend"></div><span class="shop">Shop now</span></div>
    <div class="card"><div class="ph" role="img" aria-label="Coffee bag with horse illustration, third blend"></div><span class="shop">Shop now</span></div>
    <div class="card"><div class="ph" role="img" aria-label="Coffee bag with horse illustration, fourth blend"></div><span class="shop">Shop now</span></div>
  </div>
</section>

<section class="testimonials">
  <div class="t-head">
    <div class="eyebrow">Testimonials</div>
    <h2>What people are<br>saying</h2>
  </div>
  <div class="ph" role="img" aria-label="Cartoon rider jumping a fence on horseback" style="left:850px;top:20px;width:150px;height:150px;background:#e6d2b6;border-radius:6px"></div>
  <div class="avatars" role="img" aria-label="Customer portraits"><span></span><span></span><span></span></div>
  <div class="who"><b>Mara Ellison</b><small>Customer</small></div>
  <div class="quote">
    <p>The beans arrive fresh every single time and the flavours are wonderful. Our morning routine feels brighter since we switched, and the whole family now has a favourite blend to share at the table.</p>
    <p>Friendly service, quick delivery and lovely packaging too.</p>
  </div>
  <div class="arrows">
    <span><svg viewBox="0 0 12 12"><path d="M8 2L4 6l4 4"/></svg></span>
    <span><svg viewBox="0 0 12 12"><path d="M4 2l4 4-4 4"/></svg></span>
  </div>
</section>

<section class="newsletter">
  <div class="ph" role="img" aria-label="Roasted coffee beans spilling from a wooden scoop and burlap sack"></div>
  <div class="nl-copy">
    <div class="eyebrow">Sign up newsletter</div>
    <h2>Subscribe for the exclusive<br>updates!</h2>
    <div class="nl-form"><span>Enter your email</span><b>Subscribe</b></div>
  </div>
</section>

<section class="insta">
  <div class="ph" role="img" aria-label="Cartoon horse and rider" style="left:40px;top:40px;width:110px;height:100px;background:#e6d2b6;border-radius:6px"></div>
  <div class="insta-band"><i></i>Follow us on instagram</div>
  <div class="ph" role="img" aria-label="Cartoon cowboy on horseback" style="left:1050px;top:40px;width:110px;height:100px;background:#e6d2b6;border-radius:6px"></div>
  <div class="gallery">
    <div role="img" aria-label="Iced coffee drinks" style="background:linear-gradient(160deg,#8a6b52,#3b281c)"></div>
    <div role="img" aria-label="Coffee cup with beans" style="background:linear-gradient(160deg,#e8dccb,#9a7458)"></div>
    <div role="img" aria-label="Espresso being poured" style="background:linear-gradient(160deg,#6a4a35,#2a1a10)"></div>
    <div role="img" aria-label="Latte art in a white cup" style="background:linear-gradient(160deg,#c8a27a,#6c4a30)"></div>
    <div role="img" aria-label="Barista at the counter" style="background:linear-gradient(160deg,#a68a72,#4a3424)"></div>
    <div role="img" aria-label="Whipped coffee drink" style="background:linear-gradient(160deg,#d9c2a6,#7a5638)"></div>
  </div>
</section>

<footer class="footer">
  <div class="f-intro">
    <div class="eyebrow">Contact us</div>
    <h2>Get in touch</h2>
    <p>Questions about our blends or your order? Send us a note and our small team will reply within one working day.</p>
  </div>
  <div class="f-col" style="left:520px">
    <span class="ic"><svg viewBox="0 0 24 24"><path d="M12 21s-7-6.5-7-12a7 7 0 0114 0c0 5.5-7 12-7 12z"/><circle cx="12" cy="9" r="2.5"/></svg></span>
    <div><h3>Address</h3><p>Lark House<br>48 Willow Bend Lane<br>Fernvale, OR 97000</p></div>
  </div>
  <div class="f-col" style="left:780px">
    <span class="ic"><svg viewBox="0 0 24 24"><path d="M5 4h4l2 5-2.5 1.5a11 11 0 005 5L15 13l5 2v4a2 2 0 01-2 2A16 16 0 013 6a2 2 0 012-2z"/></svg></span>
    <div><h3>Contact details</h3><p>hello@luckylarkroasters.com<br>+1 (555) 014-2278</p></div>
  </div>
  <div class="socials"><span></span><span></span><span></span><span></span></div>
  <span class="to-top"><svg viewBox="0 0 12 12"><path d="M2 8l4-4 4 4"/></svg></span>
  <div class="f-bottom">
    <span>© 2025 Lucky Lark Roasters. All rights reserved.</span>
    <ul><li>Home</li><li>Products</li><li>About us</li><li>Reviews</li><li>Contact us</li></ul>
  </div>
</footer>

</body>
</html>
```